Facebook profile image design (Circle)

We require a Facebook profile image design for an event with a photo similar to the attached.

The event name is: Marigold Lantern Gathering & Fair 2022
Dat 7 - 8 October 2022

Colours: Gold, navy blue or black, white

file must be in pdf, png and ai

Target Market(s)

authors

Font styles to use
Serif

Requirements
Must have
• Author photo and book cover

```html
<!DOCTYPE html>
<html lang="en">
<head>
<meta charset="utf-8">
<title>Marigold Lantern Gathering &amp; Fair 2022 – Profile Badge</title>
<link rel="stylesheet" href="https://fonts.googleapis.com/css2?family=Montserrat:wght@500;600;700&family=Cormorant+SC:wght@500;600&family=Open+Sans:wght@400;600&display=swap">
<style>
  :root {
    --gold-light: #f7e59a;
    --gold-mid: #e2b845;
    --gold-deep: #b8871f;
    --night: #141414;
    --ink: #0b0b0b;
    --white: #ffffff;
    --navy: #1b2340;
    --parchment: #e9dcc4;
    --scarf: #cfc9bb;
    --skin: #c49a7c;
    --jacket: #7d8277;
  }
  html, body {
    margin: 0;
    padding: 0;
    width: 1200px;
    height: 1200px;
    overflow: hidden;
    background: var(--white);
  }
  .badge {
    display: block;
    width: 1200px;
    height: 1200px;
  }
  .event-ring-text {
    font-family: "Montserrat", sans-serif;
    font-weight: 700;
    font-size: 42px;
    fill: var(--ink);
  }
  .event-date {
    font-family: "Open Sans", sans-serif;
    font-weight: 400;
    font-size: 42px;
    letter-spacing: 1px;
    fill: var(--white);
  }
  .event-name-mark {
    font-family: "Montserrat", sans-serif;
    font-weight: 600;
    font-size: 52px;
    fill: var(--gold-mid);
  }
  .book-quote {
    font-family: "Open Sans", sans-serif;
    font-size: 7px;
    fill: #2a2a2a;
  }
  .book-title {
    font-family: "Cormorant SC", serif;
    font-weight: 500;
    font-size: 34px;
    fill: #2b2620;
  }
  .book-subtitle {
    font-family: "Open Sans", sans-serif;
    font-weight: 600;
    font-size: 7px;
    fill: var(--white);
  }
  .book-author {
    font-family: "Cormorant SC", serif;
    font-weight: 600;
    font-size: 15px;
    fill: var(--white);
  }
</style>
</head>
<body>
<svg class="badge" viewBox="0 0 1200 1200" xmlns="http://www.w3.org/2000/svg">
  <defs>
    <linearGradient id="gold-ring" x1="0" y1="0" x2="1" y2="1">
      <stop offset="0" stop-color="var(--gold-deep)"/>
      <stop offset="0.35" stop-color="var(--gold-light)"/>
      <stop offset="0.6" stop-color="var(--gold-mid)"/>
      <stop offset="0.8" stop-color="var(--gold-light)"/>
      <stop offset="1" stop-color="var(--gold-deep)"/>
    </linearGradient>
    <linearGradient id="gold-star" x1="0" y1="0" x2="0" y2="1">
      <stop offset="0" stop-color="var(--gold-light)"/>
      <stop offset="1" stop-color="var(--gold-deep)"/>
    </linearGradient>
    <radialGradient id="portrait-tone" cx="0.5" cy="0.45" r="0.5">
      <stop offset="0" stop-color="var(--skin)"/>
      <stop offset="0.3" stop-color="var(--skin)"/>
      <stop offset="0.5" stop-color="var(--scarf)"/>
      <stop offset="0.78" stop-color="var(--jacket)" stop-opacity="0.85"/>
      <stop offset="1" stop-color="var(--night)" stop-opacity="0"/>
    </radialGradient>
    <linearGradient id="cover-tone" x1="0" y1="0" x2="0" y2="1">
      <stop offset="0" stop-color="#efe6d3"/>
      <stop offset="0.55" stop-color="var(--parchment)"/>
      <stop offset="1" stop-color="#c9b89a"/>
    </linearGradient>
    <radialGradient id="cover-portrait" cx="0.5" cy="0.45" r="0.5">
      <stop offset="0" stop-color="#c59a7c"/>
      <stop offset="0.45" stop-color="#e8e0c4"/>
      <stop offset="0.75" stop-color="var(--navy)" stop-opacity="0.8"/>
      <stop offset="1" stop-color="var(--parchment)" stop-opacity="0"/>
    </radialGradient>
    <clipPath id="inner-disc">
      <circle cx="555" cy="555" r="500"/>
    </clipPath>
    <path id="ring-arc" d="M 520 1104 A 510 510 0 0 0 1073 409"/>
    <path id="date-arc" d="M 136 458 A 430 430 0 0 1 444 140"/>
  </defs>

  <!-- gold ring and dark disc -->
  <circle class="ring" cx="600" cy="600" r="556" fill="url(#gold-ring)"/>
  <circle class="disc" cx="555" cy="555" r="500" fill="var(--night)"/>

  <!-- author portrait -->
  <g clip-path="url(#inner-disc)">
    <rect class="author-portrait" role="img" aria-label="Portrait photograph of the author wearing a pale headscarf and grey jacket"
          x="360" y="20" width="700" height="1100" fill="url(#portrait-tone)"/>
  </g>

  <!-- event date -->
  <text class="event-date"><textPath href="#date-arc">7 - 8 OCTOBER 2022</textPath></text>

  <!-- star -->
  <polygon class="star" fill="url(#gold-star)"
           points="250,372 265,411 307,411 273,436 286,477 250,452 214,477 227,436 193,411 235,411"/>

  <!-- event name mark -->
  <g class="event-mark">
    <text class="event-name-mark" x="237" y="580" text-anchor="middle">MARIGOLD</text>
    <text class="event-name-mark" x="237" y="636" text-anchor="middle">LANTERN</text>
  </g>

  <!-- book -->
  <g class="book">
    <rect x="108" y="708" width="244" height="380" fill="#000" opacity="0.25" rx="2"/>
    <rect x="100" y="700" width="244" height="380" fill="url(#cover-tone)"/>
    <rect x="338" y="700" width="6" height="380" fill="#b5a382"/>
    <text class="book-quote" x="220" y="721" text-anchor="middle">"You have no idea how you moved me! Bless you, sister."</text>
    <text class="book-quote" x="220" y="731" text-anchor="middle">– Dr Amara Velde, author of The Quiet Rising and</text>
    <text class="book-quote" x="220" y="741" text-anchor="middle">Mira's all-time favourite guest</text>
    <text class="book-title" x="210" y="792" text-anchor="middle">Embrace Your</text>
    <text class="book-title" x="210" y="828" text-anchor="middle">Hurdles</text>
    <rect class="cover-portrait" role="img" aria-label="Author photograph on the book cover"
          x="112" y="836" width="210" height="190" fill="url(#cover-portrait)"/>
    <circle class="cover-seal" cx="290" cy="865" r="28" fill="var(--gold-mid)"/>
    <rect x="100" y="1010" width="238" height="70" fill="var(--navy)"/>
    <text class="book-subtitle" x="219" y="1032" text-anchor="middle">HOW TO TURN ANY HURDLE INTO AN OPPORTUNITY</text>
    <rect x="118" y="1038" width="202" height="1" fill="var(--white)" opacity="0.7"/>
    <text class="book-author" x="219" y="1058" text-anchor="middle">LINA MARAVAL-HADI</text>
  </g>

  <!-- curved event title -->
  <text class="event-ring-text"><textPath href="#ring-arc" textLength="1070" lengthAdjust="spacingAndGlyphs">MARIGOLD LANTERN GATHERING &amp; FAIR 2022</textPath></text>
</svg>
</body>
</html>
```